Flyer design for new conveyancing business

A flyer to email to real estate agents for referrals for conveyancing work.
Business name "Brightfield Conveyancing"
Must give a very professional image. Preference is to use images of water etc.
must also contain the following details
Phone: 40913264
admin@brightfieldlegal.com.au
"For all your conveyancing needs from contract to completion"

Target Market(s)

people buying real estate

Industry/Entity Type

Real Estate

Font styles to use
Sans Serif

Colors
33b8a4
33a6d7
86cfc7
85cae6
0556a4

Requirements
Must have
• contact details
• clear text
Should not have
• be too busy

```html
<!DOCTYPE html>
<html lang="en">
<head>
<meta charset="utf-8">
<title>Brightfield Conveyancing – Flyer</title>
<link rel="stylesheet" href="https://fonts.googleapis.com/css2?family=Source+Sans+3:wght@400;600;700&display=swap">
<style>
  :root {
    --navy: #0556a4;
    --teal: #33b8a4;
    --band-teal: #34b9a5;
    --sky: #33a6d7;
    --sky-light: #85cae6;
    --water-deep: #2a78cf;
    --water-light: #5fb0f0;
    --paper: #ffffff;
    --stage: #eef2f5;
  }
  * { margin: 0; padding: 0; box-sizing: border-box; }
  html, body {
    width: 953px; height: 1200px; overflow: hidden;
    background: var(--stage);
    font-family: "Source Sans 3", "Myriad Pro", Arial, sans-serif;
  }
  .flyer {
    position: absolute; left: 68px; top: 24px;
    width: 653px; height: 922px;
    background: var(--paper);
    transform: scale(1.25); transform-origin: top left;
    overflow: hidden;
    box-shadow: 0 2px 10px rgba(0,0,0,.15);
  }
  .photo { position: absolute; left: 0; width: 653px; }
  .photo--top {
    top: 0; height: 235px;
    background: linear-gradient(180deg, var(--water-light) 0%, var(--water-deep) 55%, #ffffff 100%);
  }
  .photo--bottom {
    top: 768px; height: 154px;
    background: linear-gradient(180deg, #ffffff 0%, var(--water-deep) 45%, var(--water-light) 100%);
  }
  .brand {
    position: absolute; right: 31px; top: 258px; text-align: right;
  }
  .brand__name {
    color: var(--navy); font-weight: 700; font-size: 62px;
    line-height: 1; letter-spacing: 1px;
  }
  .brand__tag {
    color: var(--teal); font-weight: 600; font-size: 28px;
    letter-spacing: 4px; margin-top: 14px; line-height: 1;
  }
  .intro {
    position: absolute; left: 0; top: 403px; width: 653px; height: 244px;
    background: var(--band-teal);
  }
  .intro__text {
    position: absolute; right: 31px; top: 30px;
    color: var(--paper); font-size: 22.5px; line-height: 33px; text-align: right;
  }
  .contact {
    position: absolute; right: 33px; top: 664px; text-align: right;
    color: var(--navy); font-size: 21px; line-height: 30px; font-style: normal;
  }
  .contact__row { display: flex; justify-content: flex-end; align-items: center; gap: 7px; }
  .contact__icon { width: 19px; height: 19px; }
  .slogan {
    position: absolute; right: 33px; top: 730px;
    color: var(--teal); font-size: 16px; line-height: 20px; font-weight: 600;
  }
</style>
</head>
<body>
<main class="flyer">
  <div class="photo photo--top" role="img" aria-label="Photograph of a splashing blue water wave with bubbles"></div>

  <header class="brand">
    <h1 class="brand__name">BRIGHTFIELD</h1>
    <p class="brand__tag">CONVEYANCING</p>
  </header>

  <section class="intro">
    <p class="intro__text">Whether you're buying selling your home,<br>land or investment property, we at Brightfield<br>Conveyancing have the expertise to assist you<br>in the conveyance - and at the right price! So<br>let us be a part of your team.</p>
  </section>

  <address class="contact">
    <div class="contact__row">
      <span>40913264</span>
      <svg class="contact__icon" viewBox="0 0 20 20" aria-hidden="true">
        <circle cx="10" cy="10" r="8.6" fill="none" stroke="var(--navy)" stroke-width="1.4"/>
        <path d="M7.2 5.4 L8.6 7.8 L7.6 8.8 C8.2 10.2 9.6 11.7 11.1 12.4 L12.1 11.4 L14.5 12.8 L13.6 14.3 C10 14.4 5.6 10 5.7 6.4 Z" fill="var(--navy)"/>
      </svg>
    </div>
    <div class="contact__row">
      <span>admin@brightfieldlegal.com.au</span>
      <svg class="contact__icon" viewBox="0 0 20 20" aria-hidden="true">
        <circle cx="10" cy="10" r="8.6" fill="none" stroke="var(--navy)" stroke-width="1.4"/>
        <rect x="5.3" y="6.8" width="9.4" height="6.6" fill="none" stroke="var(--navy)" stroke-width="1.3"/>
        <path d="M5.3 6.8 L10 10.6 L14.7 6.8" fill="none" stroke="var(--navy)" stroke-width="1.3"/>
      </svg>
    </div>
  </address>

  <p class="slogan">For all your conveyancing needs from contract to completion</p>

  <div class="photo photo--bottom" role="img" aria-label="Photograph of a splashing blue water wave rising from the bottom edge"></div>
</main>
</body>
</html>
```